Copper Lane Assembly - Crossroads Waltz CD Cover

To prepare a CD Cover for the single "Crossroads Waltz" by Copper Lane Assembly.
You can hear the single here:
http://copperlaneassembly.example/listen/

The CLA logo and backdrop are also provided if you want to incorporate them into the CD cover design, though that isn't mandatory.

Song is about deciding on taking on a serious relationship, and leaving the single life behind.

Target Market(s)

Music listeners, 18-50 yrs old, into retro 80s, Tin Orchards/Surf Monks

Industry/Entity Type

Music Download

Requirements
Must have
• CLA logo
• Crossroads Waltz title
Nice to have
• Use of backdrop, or facimile
Should not have
• Too obvious on the term Crossroads Waltz

```html
<!DOCTYPE html>
<html lang="en">
<head>
<meta charset="utf-8">
<title>Copper Lane Assembly – CD Label and Cover</title>
<link rel="stylesheet" href="https://fonts.googleapis.com/css2?family=Antonio:wght@200;300&display=swap">
<style>
  :root {
    --page-bg: #ececee;
    --night-deep: #0c0a30;
    --night-mid: #1b2a7c;
    --night-glow: #3a54c2;
    --snow: #f7f7f7;
    --snow-shade: #e6e6e8;
    --ink-navy: #1f3472;
    --title-white: #ffffff;
  }
  * { margin: 0; padding: 0; box-sizing: border-box; }
  html, body {
    width: 1200px;
    height: 734px;
    overflow: hidden;
    background: var(--page-bg);
  }
  .disc-label {
    position: absolute;
    left: 28px;
    top: 112px;
    width: 524px;
    height: 524px;
  }
  .cover {
    position: absolute;
    left: 588px;
    top: 88px;
    width: 568px;
    height: 566px;
  }
  .band-word {
    font-family: "Antonio", sans-serif;
    font-weight: 300;
    text-transform: uppercase;
  }
  .band-word--light { fill: var(--title-white); }
  .band-word--dark { fill: var(--ink-navy); }
  .sky-edge { stop-color: var(--night-deep); }
  .sky-centre { stop-color: var(--night-mid); }
  .sky-glow { stop-color: var(--night-glow); }
  .sky-glow-fade { stop-color: var(--night-glow); stop-opacity: 0; }
  .ground-light { stop-color: var(--snow); }
  .ground-shade { stop-color: var(--snow-shade); }
  .figures-light { fill: var(--title-white); }
  .figures-reflection { fill: var(--ink-navy); }
  .outline { fill: none; stroke: var(--ink-navy); }
  .spindle-hole { fill: var(--title-white); }
</style>
</head>
<body>
  <svg width="0" height="0" aria-hidden="true" style="position:absolute">
    <defs>
      <linearGradient id="sky-band" x1="0" y1="0" x2="1" y2="0">
        <stop offset="0" class="sky-edge"/>
        <stop offset="0.45" class="sky-centre"/>
        <stop offset="0.7" class="sky-centre"/>
        <stop offset="1" class="sky-edge"/>
      </linearGradient>
      <radialGradient id="sky-glow" cx="0.45" cy="0.25" r="0.55">
        <stop offset="0" class="sky-glow"/>
        <stop offset="1" class="sky-glow-fade"/>
      </radialGradient>
      <radialGradient id="ground-fade" cx="0.5" cy="0.35" r="0.8">
        <stop offset="0" class="ground-light"/>
        <stop offset="1" class="ground-shade"/>
      </radialGradient>
      <clipPath id="disc-shape"><circle cx="262" cy="262" r="261"/></clipPath>
    </defs>
  </svg>

  <svg class="disc-label" viewBox="0 0 524 524" aria-label="CD disc label">
    <g clip-path="url(#disc-shape)">
      <rect x="0" y="0" width="524" height="262" fill="url(#sky-band)" role="img" aria-label="Night sky backdrop with glowing bokeh lights"/>
      <rect x="0" y="0" width="524" height="262" fill="url(#sky-glow)"/>
      <rect x="0" y="262" width="524" height="262" fill="url(#ground-fade)"/>
      <rect class="figures-light" x="306" y="82" width="116" height="182" rx="30" role="img" aria-label="White silhouette of a couple walking away hand in hand"/>
      <rect class="figures-reflection" x="306" y="264" width="66" height="192" rx="24" role="img" aria-label="Navy reflection of the walking man below the horizon"/>
      <text class="band-word band-word--light" x="62" y="218" font-size="100" textLength="154" lengthAdjust="spacingAndGlyphs">Copper</text>
      <text class="band-word band-word--dark" x="62" y="312" font-size="83" textLength="154" lengthAdjust="spacingAndGlyphs">Lane</text>
      <text class="band-word band-word--dark" x="62" y="378" font-size="61" textLength="157" lengthAdjust="spacingAndGlyphs">Assembly</text>
    </g>
    <circle class="spindle-hole" cx="262" cy="262" r="32"/>
    <circle class="outline" cx="262" cy="262" r="261" stroke-width="2"/>
  </svg>

  <svg class="cover" viewBox="0 0 568 566" aria-label="CD front cover">
    <rect x="0" y="0" width="568" height="284" fill="url(#sky-band)" role="img" aria-label="Night sky backdrop with glowing bokeh lights"/>
    <rect x="0" y="0" width="568" height="284" fill="url(#sky-glow)"/>
    <rect x="0" y="284" width="568" height="282" fill="url(#ground-fade)"/>
    <rect class="figures-light" x="340" y="44" width="152" height="244" rx="40" role="img" aria-label="White silhouette of a couple walking away hand in hand"/>
    <rect class="figures-reflection" x="340" y="288" width="88" height="256" rx="30" role="img" aria-label="Navy reflection of the walking man below the horizon"/>
    <text class="band-word band-word--light" x="62" y="218" font-size="165" textLength="243" lengthAdjust="spacingAndGlyphs">Copper</text>
    <text class="band-word band-word--dark" x="62" y="364" font-size="148" textLength="243" lengthAdjust="spacingAndGlyphs">Lane</text>
    <text class="band-word band-word--dark" x="62" y="468" font-size="98" textLength="248" lengthAdjust="spacingAndGlyphs">Assembly</text>
    <rect class="outline" x="0.5" y="0.5" width="567" height="565" stroke-width="1"/>
  </svg>
</body>
</html>
```